Rum Label design

Already have my logo design, as well as text written. We are now needing someone to design the label for our Rum line. Ideas on paper, font, colors, etc. Straight forward work. Can provided the text upon request. The rum, is called "Tallwick Rum" and label has to have a mix of caribbean feel as well as "country boy" appeal...believe the use of paper, color etc will be most important element.

Reason: We've extended the deadline in order to get more submissions....thanks everyone who has so far submitted ideas. We'll be posting to every one shortly...

```html
<!DOCTYPE html>
<html lang="en">
<head>
<meta charset="utf-8">
<title>Tallwick Rum – Back Label</title>
<link rel="stylesheet" href="https://fonts.googleapis.com/css2?family=Amatic+SC:wght@400;700&family=Mr+Dafoe&display=swap">
<style>
  :root {
    --backdrop: #2a2320;
    --paper: #ece4d2;
    --paper-edge: #ddd2bb;
    --ink: #1d1a17;
    --rum-red: #c8242c;
    --caribbean-teal: #3aa7c4;
    --palm-ink: #1d1a17;
  }
  * { box-sizing: border-box; margin: 0; padding: 0; }
  html, body { width: 1200px; height: 920px; overflow: hidden; }
  body {
    background: var(--backdrop);
    font-family: "Amatic SC", "Arial Narrow", sans-serif;
    color: var(--ink);
  }
  .back-label {
    position: absolute;
    left: 280px; top: 30px;
    width: 640px; height: 860px;
    background: radial-gradient(ellipse at 50% 40%, var(--paper) 60%, var(--paper-edge) 100%);
    box-shadow: 0 10px 30px rgba(0,0,0,.45);
  }
  .label-frame { position: absolute; inset: 0; width: 640px; height: 860px; }
  .corner-star { position: absolute; width: 40px; height: 40px; bottom: 14px; }
  .corner-star--left { left: 8px; }
  .corner-star--right { right: 8px; }

  .label-content {
    position: absolute; left: 60px; right: 60px; top: 44px;
    text-align: center; font-weight: 700;
  }
  .warning-title {
    display: flex; align-items: center; gap: 10px;
    font-size: 30px; line-height: 1; margin-left: 0; margin-bottom: 18px;
  }
  .warning-title svg { width: 36px; height: 32px; }
  .warning-copy { font-size: 20px; line-height: 1.2; margin-bottom: 14px; }
  .certificate-line { text-align: left; font-size: 20px; margin-top: 14px; }
  .signature {
    font-family: "Mr Dafoe", cursive; font-weight: 400;
    color: var(--rum-red); font-size: 84px; line-height: 1;
    margin: 0 0 40px 150px; text-align: left;
  }
  .government-warning { display: flex; gap: 14px; text-align: left; margin-bottom: 30px; }
  .warning-icons { display: flex; flex-direction: column; gap: 12px; padding-top: 2px; }
  .warning-icons svg { width: 36px; height: 36px; }
  .government-warning p { font-size: 17.5px; line-height: 1.2; }

  .volume-row { display: flex; align-items: flex-end; justify-content: space-between; margin-bottom: 22px; }
  .volume { text-align: left; font-size: 24px; line-height: 1.15; }
  .palm-island {
    width: 66px; height: 58px; margin-right: 40px;
    background: linear-gradient(180deg, #3a3431, var(--palm-ink));
    border-radius: 40% 40% 10% 10%;
  }
  .batch-code { font-size: 19px; letter-spacing: .45em; width: 250px; text-align: center; }
  .origin { color: var(--caribbean-teal); font-size: 20px; letter-spacing: .06em; margin-bottom: 10px; }
  .legal-lines { font-size: 14px; line-height: 1.25; }
</style>
</head>
<body>
  <main class="back-label">
    <svg class="label-frame" viewBox="0 0 640 860" aria-hidden="true">
      <path d="M22 62 A40 40 0 0 0 62 22 H578 A40 40 0 0 0 618 62 V798 A40 40 0 0 0 578 838 H62 A40 40 0 0 0 22 798 Z"
            fill="none" stroke="#1d1a17" stroke-width="4"/>
      <path d="M34 80 A48 48 0 0 0 80 34 H560 A48 48 0 0 0 606 80 V780 A48 48 0 0 0 560 826 H80 A48 48 0 0 0 34 780 Z"
            fill="none" stroke="#1d1a17" stroke-width="1.5"/>
    </svg>
    <svg class="corner-star corner-star--left" viewBox="0 0 40 40" aria-hidden="true">
      <polygon points="20,2 25,15 39,15 28,24 32,38 20,29 8,38 12,24 1,15 15,15" fill="#c8242c"/>
    </svg>
    <svg class="corner-star corner-star--right" viewBox="0 0 40 40" aria-hidden="true">
      <polygon points="20,2 25,15 39,15 28,24 32,38 20,29 8,38 12,24 1,15 15,15" fill="#c8242c"/>
    </svg>

    <div class="label-content">
      <h1 class="warning-title">
        <svg viewBox="0 0 36 32" aria-hidden="true">
          <polygon points="18,1 35,31 1,31" fill="#c8242c"/>
          <rect x="16" y="10" width="4" height="12" fill="#ece4d2"/>
          <rect x="16" y="24" width="4" height="4" fill="#ece4d2"/>
        </svg>
        !Warning!
      </h1>
      <p class="warning-copy">Do not use this product for clean'n tools, bath'n, paint removin or dog shampoo.</p>
      <p class="warning-copy">Excessive use may result in an outbreak of temporary blindness and/or lapse in judgement if members of the opposite sex are involved and/or possible jail time. Consult your local police for details.</p>
      <p class="warning-copy">Tallwick Rum is not responsible for any unwanted children, loss of horse or farmin equipment due to the use of this product. Sorry ya'll on your own!</p>
      <p class="certificate-line">Certificate of the Tallwick bottling this stuff</p>
      <p class="signature">Cal Hollis</p>

      <section class="government-warning">
        <div class="warning-icons">
          <svg viewBox="0 0 36 36" aria-label="No drinking while pregnant" role="img">
            <circle cx="18" cy="18" r="15" fill="none" stroke="#c8242c" stroke-width="3"/>
            <line x1="7" y1="7" x2="29" y2="29" stroke="#c8242c" stroke-width="3"/>
          </svg>
          <svg viewBox="0 0 36 36" aria-label="Recyclable" role="img">
            <path d="M18 5 L26 18 H10 Z M8 22 L16 31 H4 Z M28 22 L32 31 H20 Z" fill="#1d1a17"/>
          </svg>
        </div>
        <p>Government warning (1) according to the surgeon general, women should not drink alcoholic beverages during pregnancy because of the risk of birth defects. (2) Consumption of alcoholic beverages impairs your ability to drive a car or operate machinery and may cause health issues.</p>
      </section>

      <div class="volume-row">
        <p class="volume">700mL<br>37.5% ALC/VOL</p>
        <div class="palm-island" role="img" aria-label="Small palm tree island illustration"></div>
        <p class="batch-code">Tallwick - Rum - 2014</p>
      </div>

      <p class="origin">Product of the Dominican Republic</p>
      <div class="legal-lines">
        <p>Produced by Marrow Ltd in conjunction with Pruett &amp; Pruett of Santo Domingo, Dominican Republic</p>
        <p>Produced by authority and under the supervision of Marrow Ltd.</p>
        <p>Tallwick Rum and the pig device are registered trademarks of Marrow Ltd.</p>
      </div>
    </div>
  </main>
</body>
</html>
```